SEO Agentur www.findeprofi.de - Webseite soll neu designed werden (Start- und Unterseite)
Zielgruppe
Alle Infos sind auf der Seite www.findeprofi.de enthalten.
Aufgabenstellung
Die Seite soll neu gestalltet werden. Wir möchten gerne ein wenig professioneller werden. Der Name der Seite zwingt uns allerdings ein gewisses Thema auf.
Die Aufgabe:
Ein professionelleres Design der Startseite und einer Unterseite. Die Programmierung machen wir selbst. Thema Suche und Helden muss bleiben aufgrund der URL.
Mit dem Gewinner würden wir dann auch geren jedes Element der Seite durchgehen und neu gestallten (separater Auftrag).
Das Blitzwolf Logo ist aufgrund des neuen Films auch gewaltiger und seriöser geworden. Vielleicht kann man daran anknüpfen. Ist aber keine Bedingung nur eine kleine Idee.
Wir werden alle Vorschläge ca. 50 Leuten vorstellen und dann den Vorschlag mit den meisten Stimmen wählen.

```html
<!DOCTYPE html>
<html lang="de">
<head>
<meta charset="utf-8">
<title>findeprofi.de – SEO Agentur</title>
<link href="https://fonts.googleapis.com/css2?family=Source+Sans+3:wght@300;400;600;700&display=swap" rel="stylesheet">
<style>
:root{
  --blue:#0090dc;
  --nav-blue:#0a96e3;
  --dark:#2b2b2b;
  --ink:#222;
  --white:#fff;
  --hero-light:#f3f4f4;
  --hero-mid:#dfe2e3;
}
*{margin:0;padding:0;box-sizing:border-box}
html,body{width:1159px;height:1200px;overflow:hidden;background:var(--white)}
body{position:relative;font-family:"Source Sans 3",sans-serif;color:var(--ink)}
.abs{position:absolute}

/* hero */
.hero{left:0;top:0;width:1159px;height:384px;background:linear-gradient(180deg,var(--hero-light),var(--hero-mid))}
.hero-people{left:228px;top:215px;width:240px;height:169px;background:linear-gradient(160deg,#3a3a3a,#2a2a2a);border-radius:40px 60px 0 0;opacity:.9}
.hero-crowd{left:555px;top:8px;width:440px;height:376px;background:linear-gradient(180deg,#3b3b3b,#2b2b2b);border-radius:120px 120px 0 0;opacity:.88}
.brand{left:194px;top:40px;display:flex;align-items:center;gap:10px;font-weight:700;font-size:24px;color:var(--ink)}
.brand-mark{width:28px;height:28px;background:var(--blue);flex:none}
.nav{left:458px;top:16px;display:flex;height:45px;background:var(--nav-blue)}
.nav a{color:#111;text-decoration:none;font-size:14px;line-height:45px;padding:0 9px;border-right:1px solid #5bbcf0}
.nav a:last-child{border-right:none}

/* intro */
.intro{left:0;top:384px;width:1159px;height:361px;background:var(--dark)}
.headline{left:192px;top:437px;font-weight:300;font-size:38px;line-height:50px;color:var(--white)}
.intro-sub{left:194px;top:550px;font-weight:600;font-size:18px;color:var(--blue)}
.intro-text{left:194px;top:590px;width:400px;font-size:12.5px;line-height:20px;color:var(--white)}
.intro-icons{left:495px;top:425px}
.hotline{left:822px;top:537px;color:var(--white)}
.hotline h2{font-size:28px;font-weight:700;color:var(--blue);line-height:34px}
.hotline .phone{font-size:13px;font-weight:700;margin-top:2px}
.hotline .day{font-size:12px;font-weight:700;color:var(--blue);margin-top:10px;line-height:15px}
.hotline .time{font-size:10px;font-weight:600;line-height:14px}

/* features */
.features{left:0;top:745px;width:1159px;height:300px;background:var(--blue)}
.feature{top:783px;width:230px;color:var(--white)}
.feature-head{display:flex;align-items:center;gap:16px;height:36px}
.feature-head h3{font-size:16px;font-weight:600}
.feature p{margin-top:18px;font-size:12px;line-height:20px;width:205px;height:120px}
.btn{display:inline-block;margin-top:18px;border:1px solid var(--white);color:var(--white);font-size:12.5px;padding:5px 14px;text-decoration:none}

/* footer */
.foot-brand{left:196px;top:1118px;display:flex;align-items:center;gap:5px;font-weight:700;font-size:12px}
.foot-brand .brand-mark{width:12px;height:12px}
.foot-col{top:1114px;font-size:10.5px;font-weight:600;line-height:15px}
.social{left:643px;top:1114px;display:flex;flex-direction:column;gap:1px;font-size:10px;font-weight:600;line-height:14px}
.social span{display:flex;align-items:center;gap:4px}
.social i{width:9px;height:9px;background:var(--ink);display:inline-block}
.msg{left:744px;top:1117px;width:150px;height:28px;border:1px solid var(--ink);font-size:12.5px;font-weight:600;line-height:26px;text-align:center}
.copy{left:195px;top:1180px;font-size:9px;color:#444}
</style>
</head>
<body>
<div class="abs hero" role="img" aria-label="Heller, unscharfer Büro-Hintergrund"></div>
<div class="abs hero-people" role="img" aria-label="Silhouetten zweier Geschäftsleute am Laptop"></div>
<div class="abs hero-crowd" role="img" aria-label="Silhouetten einer Gruppe von Geschäftsleuten"></div>

<div class="abs brand"><span class="brand-mark"></span>findeprofi.de</div>

<nav class="abs nav">
  <a href="#">ABLAUF</a><a href="#">VORTEILE</a><a href="#">LEISTUNGEN</a><a href="#">100% GARANTIE</a><a href="#">INFOS</a><a href="#">BLOG</a><a href="#">KONTAKT</a>
</nav>

<section class="abs intro"></section>
<h1 class="abs headline">Die richtige<br>Zielgruppe finden</h1>
<svg class="abs intro-icons" width="270" height="80" viewBox="0 0 270 80" fill="#fff" stroke="#fff">
  <g stroke-width="1">
    <circle cx="34" cy="47" r="8"/>
    <circle cx="34" cy="22" r="4"/><circle cx="34" cy="72" r="4"/>
    <circle cx="9" cy="47" r="4"/><circle cx="59" cy="47" r="4"/>
    <circle cx="16" cy="29" r="4"/><circle cx="52" cy="29" r="4"/>
    <circle cx="16" cy="65" r="4"/><circle cx="52" cy="65" r="4"/>
    <path d="M34 26V39M34 55V68M13 47H26M42 47H55M19 32L28 41M49 32L40 41M19 62L28 53M49 62L40 53" fill="none"/>
  </g>
  <circle cx="97" cy="31" r="5"/><circle cx="205" cy="31" r="5"/>
  <path d="M102 31C125 30 118 68 134 64C150 60 140 30 160 36C178 42 170 68 186 56C194 48 196 36 200 32" fill="none" stroke-dasharray="3 3" stroke-width="1.2"/>
  <rect x="232" y="4" width="34" height="22" rx="2" fill="none" stroke-width="3"/>
  <path d="M249 26V31M242 32H256" stroke-width="2.5"/>
</svg>
<div class="abs intro-sub">Erfolgsbasiert und mit 100% Geld zurück Garantie</div>
<p class="abs intro-text">Wir von Findeprofi.de haben uns auf die Suchmaschinenoptimierung Ihrer Website spezialisiert. Wir helfen Ihnen, dass Sie bei Findora &amp; Co. in den Suchergebnissen ganz vorne gerankt werden. Mit unserer Hilfe steigern Sie Ihre Besucherzahlen, Ihre Kundenzahlen, Ihr Image und schlussendlich auch Ihre Umsätze. Bei uns erhalten Sie online Marketing aus einer Hand.</p>
<div class="abs hotline">
  <h2>Hotline</h2>
  <div class="phone">0541 - 555 018 27</div>
  <div class="day">Montag – Donnerstag</div>
  <div class="time">08:00 – 12:00 Uhr / 13:30 – 17:00 Uhr</div>
  <div class="day" style="margin-top:6px">Freitag</div>
  <div class="time">8:00 – 12:00 Uhr</div>
</div>

<section class="abs features"></section>
<article class="abs feature" style="left:192px">
  <div class="feature-head">
    <svg width="42" height="30" viewBox="0 0 42 30" fill="#fff" stroke="#fff"><rect x="15" y="12" width="12" height="12"/><circle cx="21" cy="3" r="2.5"/><circle cx="8" cy="6" r="2.5"/><circle cx="34" cy="6" r="2.5"/><circle cx="3" cy="18" r="2.5"/><circle cx="39" cy="18" r="2.5"/><path d="M21 5V12M9 8L15 13M33 8L27 13M5 18H15M37 18H27M17 24L13 29M25 24L29 29" fill="none"/></svg>
    <h3>Was ist SEO?</h3>
  </div>
  <p>Kurz gesagt: Mehr Kunden und mehr Umsatz! Unter dem Begriff SEO versteht sich ein technischer Prozess der Ihnen zu einer nachhaltigen Ver­besserung bei den Suchergebnissen verhilft.</p>
  <a class="btn" href="#">&gt;&gt; mehr erfahren</a>
</article>
<article class="abs feature" style="left:468px">
  <div class="feature-head">
    <svg width="36" height="36" viewBox="0 0 36 36" fill="#fff" stroke="#fff"><path d="M2 2V34H34" fill="none" stroke-width="2"/><rect x="8" y="22" width="4" height="10"/><rect x="15" y="18" width="4" height="14"/><rect x="22" y="14" width="4" height="18"/><rect x="29" y="10" width="4" height="22"/><path d="M7 18L16 10L22 13L32 4" fill="none" stroke-width="2"/></svg>
    <h3>Nur die Top 10 zählen</h3>
  </div>
  <p>Mehr als 95% der Findora Nutzer schenken statistisch bewiesen lediglich den ersten 10 Positionen Beachtung. Wie ist es bei Ihnen?</p>
  <a class="btn" href="#">&gt;&gt; mehr erfahren</a>
</article>
<article class="abs feature" style="left:740px">
  <div class="feature-head">
    <svg width="36" height="36" viewBox="0 0 36 36"><circle cx="18" cy="18" r="18" fill="#fff"/><path d="M13 16V10M11 12L13 10L15 12M18 16V8M16 10L18 8L20 10M23 16V10M21 12L23 10L25 12" stroke="#0090dc" stroke-width="1.4" fill="none"/><text x="18" y="26" font-size="8" font-weight="700" fill="#0090dc" text-anchor="middle" font-family="Source Sans 3, sans-serif">SEO</text></svg>
    <h3>Unsere Garantie für Sie</h3>
  </div>
  <p>Sollten Ihre vorab festgelegten Suchbegriffe gegen alle Erwartun­gen nicht innerhalb von 6 Monaten unter den TOP 10 bei den Such­ergebnissen von Findora gelistet sein.</p>
  <a class="btn" href="#">&gt;&gt; mehr erfahren</a>
</article>

<footer>
  <div class="abs foot-brand"><span class="brand-mark"></span>findeprofi.de</div>
  <div class="abs foot-col" style="left:295px">Findeprofi.de GbR<br>Lindenweg 12</div>
  <div class="abs foot-col" style="left:444px">49100 Musterstadt<br>0541 - 555 018 27</div>
  <div class="abs social"><span><i></i>Vidora</span><span><i></i>Kontaktnetz</span></div>
  <div class="abs msg">Nachricht senden &gt;&gt;</div>
  <div class="abs copy">Copyright © 2014 Findeprofi.de • All rights reserved • Impressum</div>
</footer>
</body>
</html>
```